I'm a family owned and operated electrical contractor in Colorado USA. We offer a full electrical service, remodel and new construction, we also offer energy saving solutions like LED lighting, photo voltaic, and wind energy,
We sell and install BrightNova light fixtures (rbightNova.com)
More information about my business can be looked at my website copperpeakelcetric.com My logo is on my website.

Industry/Entity Type

Electrical

Contact Information for Business Card

Copper Peak Electric, Dwight Sorensby, Owner, BrightNova Sale & Install, Full Electrical Service, Remodel & New Construction. P: 303-512-8847 F:303-264-3318 E:dwight@copperpeakelectric.com, 27519 CR41, Cedarvale, WY 80194

```html
<!DOCTYPE html>
<html lang="en">
<head>
<meta charset="utf-8">
<title>Copper Peak Electric – Business Card</title>
<link rel="stylesheet" href="https://fonts.googleapis.com/css2?family=Arimo:ital,wght@0,400;0,700;1,400&display=swap">
<style>
  :root {
    --stage: #1d2122;
    --lime: #8cff00;
    --lime-light: #a8ff2a;
    --lime-deep: #7fe600;
    --charcoal: #1b1b1b;
    --charcoal-light: #363636;
    --white: #ffffff;
    --soft-white: #f1f1f1;
  }
  * { margin: 0; padding: 0; box-sizing: border-box; }
  html, body {
    width: 1200px; height: 733px; overflow: hidden;
    background: var(--stage);
    font-family: "Arimo", Arial, sans-serif;
  }
  .canvas {
    position: relative; width: 1200px; height: 733px;
    display: flex; align-items: center; justify-content: center; gap: 26px;
  }
  .card {
    position: relative; width: 560px; height: 327px; overflow: hidden;
    box-shadow: 0 10px 30px rgba(0,0,0,.45);
  }

  /* Front */
  .card-front {
    background: radial-gradient(circle at 55% 45%, var(--lime-light), var(--lime) 55%, var(--lime-deep));
    display: flex; align-items: center; justify-content: center;
  }
  .brand { display: flex; align-items: center; gap: 12px; }
  .brand-dot { width: 30px; height: 30px; border-radius: 50%; background: var(--white); flex: none; }
  .brand-name {
    color: var(--white); font-weight: 700; font-size: 27px;
    letter-spacing: 1px; text-transform: uppercase; white-space: nowrap;
  }

  /* Back */
  .card-back {
    background: radial-gradient(circle at 65% 40%, var(--charcoal-light), var(--charcoal) 70%);
  }
  .back-brand {
    position: absolute; left: 35px; top: 100px; gap: 9px;
  }
  .back-brand .brand-dot { width: 18px; height: 18px; background: var(--soft-white); }
  .back-brand .brand-name { font-size: 16px; letter-spacing: 1.2px; color: var(--soft-white); }

  .services { position: absolute; left: 35px; top: 188px; list-style: none; }
  .services li {
    display: flex; align-items: center; gap: 4px;
    color: var(--white); font-style: italic; font-size: 14px;
    height: 24px; margin-bottom: 8.5px; white-space: nowrap;
  }
  .bulb { width: 13px; height: 22px; flex: none; }

  .contact-panel {
    position: absolute; left: 300px; top: 0; right: 0; bottom: 0;
    background: radial-gradient(circle at 70% 45%, var(--lime-light), var(--lime) 60%);
    border-radius: 58px 0 0 58px;
    color: var(--white); padding-left: 21px;
  }
  .person-name { position: absolute; top: 48px; font-size: 19px; font-weight: 700; white-space: nowrap; }
  .person-role { position: absolute; top: 72px; font-size: 14.5px; }
  .contact-block { position: absolute; font-size: 13px; line-height: 19.5px; left: 23px; white-space: nowrap; }
  .address { top: 119px; }
  .lines { top: 183px; }
  .website { top: 265px; text-decoration: underline; }
</style>
</head>
<body>
<main class="canvas">
  <section class="card card-front" aria-label="Card front">
    <div class="brand">
      <span class="brand-dot"></span>
      <span class="brand-name">Copper Peak Electric</span>
    </div>
  </section>

  <section class="card card-back" aria-label="Card back">
    <div class="brand back-brand">
      <span class="brand-dot"></span>
      <span class="brand-name">Copper Peak Electric</span>
    </div>

    <ul class="services">
      <li><svg class="bulb" viewBox="0 0 13 22" aria-hidden="true"><path d="M6.5 1a5.5 5.5 0 0 0-3.4 9.8c.6.5.9 1.2.9 2V14h5v-1.2c0-.8.3-1.5.9-2A5.5 5.5 0 0 0 6.5 1z" fill="#fff"/><rect x="4" y="15" width="5" height="1.4" fill="#ddd"/><rect x="4" y="17.2" width="5" height="1.4" fill="#ddd"/><rect x="5" y="19.4" width="3" height="1.4" fill="#ddd"/></svg>BrightNova Sale &amp; Insall</li>
      <li><svg class="bulb" viewBox="0 0 13 22" aria-hidden="true"><path d="M6.5 1a5.5 5.5 0 0 0-3.4 9.8c.6.5.9 1.2.9 2V14h5v-1.2c0-.8.3-1.5.9-2A5.5 5.5 0 0 0 6.5 1z" fill="#fff"/><rect x="4" y="15" width="5" height="1.4" fill="#ddd"/><rect x="4" y="17.2" width="5" height="1.4" fill="#ddd"/><rect x="5" y="19.4" width="3" height="1.4" fill="#ddd"/></svg>Full Electrical Service</li>
      <li><svg class="bulb" viewBox="0 0 13 22" aria-hidden="true"><path d="M6.5 1a5.5 5.5 0 0 0-3.4 9.8c.6.5.9 1.2.9 2V14h5v-1.2c0-.8.3-1.5.9-2A5.5 5.5 0 0 0 6.5 1z" fill="#fff"/><rect x="4" y="15" width="5" height="1.4" fill="#ddd"/><rect x="4" y="17.2" width="5" height="1.4" fill="#ddd"/><rect x="5" y="19.4" width="3" height="1.4" fill="#ddd"/></svg>Remodel &amp; New Construction</li>
    </ul>

    <div class="contact-panel">
      <h1 class="person-name">Dwight Sorensby</h1>
      <p class="person-role">Owner</p>
      <p class="contact-block address">27519 CR41<br>Cedarvale, WY 80194</p>
      <p class="contact-block lines">P 303.512.8847<br>F 303.264.3318<br>E dwight@copperpeakelectric.com</p>
      <p class="contact-block website">www.copperpeakelectric.com</p>
    </div>
  </section>
</main>
</body>
</html>
```